Powerpoint Presentation design template

I am looking for a PPT presentation that show class and professionalism and in the same colour them as the logo. It should be simple, but yet classy and pro. The business is an oil and gas exploration and exploitation business. The business has nothing to do with solar panel and other renewable energies, so please no solar panel or wind farms in the background. It would be more oil rigs and LNG plant in the background of some slide templates...

oil and gas exploration and exploitation

```html
<!DOCTYPE html>
<html lang="en">
<head>
<meta charset="utf-8">
<title>Basalt Energy – Presentation Slides</title>
<link href="https://fonts.googleapis.com/css2?family=Poppins:wght@300;400;500;600;700;800&display=swap" rel="stylesheet">
<style>
  :root{
    --navy:#0b1a5e;
    --blue:#1a8fd0;
    --ink:#111a3d;
    --text:#5b5f6b;
    --line:#e3e6ee;
    --page:#ffffff;
    --icon:#6b6e74;
  }
  *{box-sizing:border-box;margin:0;padding:0}
  html,body{width:1200px;height:3324px;overflow:hidden;background:var(--page);font-family:"Poppins",sans-serif}
  .slide{position:absolute;left:72px;width:1045px;height:587px;background:#fff;overflow:hidden;box-shadow:0 10px 30px rgba(20,30,60,.22)}
  .s1{top:74px}.s2{top:715px}.s3{top:1355px}.s4{top:1995px}.s5{top:2634px}
  .photo{position:absolute}

  /* slide 1 */
  .s1 .band{position:absolute;left:0;top:0;width:229px;height:100%;background:var(--navy)}
  .s1 .rig-main{left:69px;top:60px;width:323px;height:527px;background:linear-gradient(180deg,#8fb4d6 0%,#b9c9d6 40%,#7a3b34 75%,#3e5f7e 100%)}
  .s1 .rig-side{left:405px;top:0;width:151px;height:494px;background:linear-gradient(180deg,#88aed2 0%,#c0cdd6 45%,#6b3a33 80%,#2f3f52 100%)}
  .price{position:absolute;left:319px;top:471px;width:203px;height:83px;background:#fff;text-align:center;padding-top:12px;box-shadow:0 2px 8px rgba(0,0,0,.08)}
  .price .amount{font-size:28px;font-weight:500;color:var(--navy);line-height:1.1}
  .price .amount sup{font-size:14px;vertical-align:10px}
  .price .label{font-size:11px;font-weight:700;letter-spacing:2px;color:var(--blue);margin-top:4px}
  .s1 .copy{position:absolute;left:616px;top:84px;width:370px}
  .s1 h1{font-size:27px;font-weight:700;color:var(--navy);line-height:1.4;margin-bottom:16px}
  .s1 p{font-size:12.5px;line-height:23.5px;color:var(--text);margin-bottom:10px}

  /* logo lockup */
  .brand{position:absolute;display:flex;align-items:center;justify-content:center;gap:9px;background:#fff;box-shadow:0 2px 10px rgba(0,0,0,.1);font-size:15px;font-weight:700;color:var(--navy);letter-spacing:.5px}
  .brand .dot{width:22px;height:22px;border-radius:50%;background:var(--blue)}

  /* slide 2 */
  .s2 h2{position:absolute;left:83px;top:66px;width:580px;font-size:22px;font-weight:600;line-height:31px;color:var(--ink)}
  .s2 h2 span{color:var(--blue)}
  .s2 .brand{left:790px;top:53px;width:179px;height:75px}
  .table-card{position:absolute;left:77px;top:155px;width:890px;height:390px;background:#fff;box-shadow:0 2px 12px rgba(0,0,0,.08);padding:19px 28px}
  table.stats{width:834px;border-collapse:collapse;table-layout:fixed}
  .stats th,.stats td{border:1px solid var(--line);text-align:center}
  .stats th{height:55px;font-size:13px;font-weight:600;color:var(--blue);line-height:16px}
  .stats td{height:37.5px;font-size:11.5px;color:var(--text);line-height:13px}

  /* slide 3 */
  .s3 .worker{left:0;top:0;width:436px;height:587px;background:linear-gradient(160deg,#5f7fb0 0%,#c08a74 30%,#3a3f4f 60%,#8c2a26 100%)}
  .s3 .brand{left:807px;top:37px;width:166px;height:70px}
  .s3 h2{position:absolute;left:487px;top:112px;font-size:34px;font-weight:600;color:var(--navy)}
  .s3 .intro{position:absolute;left:487px;top:176px;width:480px;font-size:12.5px;line-height:24px;color:var(--text)}
  .contact{position:absolute;left:436px;top:287px;width:609px;height:226px;background:var(--navy);color:#fff}
  .contact .row{position:absolute;left:62px;display:flex;align-items:center;height:30px;font-size:17px}
  .contact .row svg{width:30px;height:30px;margin-right:19px}
  .contact .key{width:93px;font-weight:600}
  .contact .r1{top:39px}.contact .r2{top:93px}.contact .r3{top:147px}

  /* slide 4 */
  .s4 h2{position:absolute;left:0;width:100%;top:34px;text-align:center;font-size:34px;font-weight:600;color:var(--navy)}
  .icon-grid{position:absolute;left:54px;top:124px;width:931px;display:grid;grid-template-columns:repeat(12,1fr);row-gap:36px;justify-items:center}
  .icon-grid .icon{width:50px;height:50px;border-radius:8px;background:var(--icon);opacity:.85}

  /* slide 5 */
  .s5 .night{left:0;top:0;width:100%;height:100%;background:radial-gradient(ellipse at 70% 20%,#a86a2a 0%,transparent 40%),radial-gradient(ellipse at 40% 45%,#8a5a28 0%,transparent 35%),linear-gradient(180deg,#1c2a5a 0%,#15236a 55%,#0d1a66 100%)}
  .closing{position:absolute;left:0;width:100%;top:238px;text-align:center;color:#fff}
  .closing h2{font-size:58px;font-weight:800;letter-spacing:1px;line-height:66px}
  .closing p{font-size:15px;letter-spacing:3.5px;margin-top:4px}
</style>
</head>
<body>

<section class="slide s1">
  <div class="band"></div>
  <div class="photo rig-main" role="img" aria-label="Offshore oil rig with cranes against a blue sky"></div>
  <div class="photo rig-side" role="img" aria-label="Close view of offshore drilling rig crane"></div>
  <div class="price">
    <div class="amount"><sup>$</sup>394.000</div>
    <div class="label">PROJECT PRICE</div>
  </div>
  <div class="copy">
    <h1>Meridian Corporation<br>Project Building</h1>
    <p>Maecenas eu varius risus, eu et arcu. Curabitur fermentum suscipit est, tincidunt mattis lorem luctus id. Donec eget massa a diam condimentum pretium. molestie semper laoreet, quam leo commodo massa, in mollis sem urna et ante. In pretium.</p>
    <p>Lorem ipsum dolor sit amet, consectetur adipiscing elit. Nunc rutrum, orci molestie semper laoreet, quam leo commodo massa, in mollis sem urna et ante. In pretium.</p>
    <p>Fusce vehicula dolor arcu, sit amet blandit dolor mollis nec. Donec viverra eleifend lacus, vitae ullamcorper metus. Sed sollicitudin ipsum quis nunc sollicitudin ultrices. Donec euismod scelerisque ligula. Maecenas eu varius risus, eu aliquet arcu. Curabitur fermentum suscipit est</p>
  </div>
</section>

<section class="slide s2">
  <h2>Statistics on regional distribution <span>of recoverable unconventional oil resources in the world</span></h2>
  <div class="brand"><span class="dot"></span>BASALT ENERGY</div>
  <div class="table-card">
    <table class="stats">
      <colgroup><col style="width:146px"><col style="width:153px"><col style="width:135px"><col style="width:135px"><col style="width:135px"><col style="width:130px"></colgroup>
      <thead>
        <tr><th>Region</th><th>Recoverable<br>unconven</th><th>Proportion of oil<br>shale %</th><th>Proportion of<br>heavy oil %</th><th>Proportion of oil<br>sands %</th><th>Proportion of<br>tight oil %</th></tr>
      </thead>
      <tbody>
        <tr><td>North America</td><td>1502.0</td><td>46.5</td><td>21.2</td><td>26.3</td><td>6.0</td></tr>
        <tr><td>Central Asia - Russia</td><td>960.9</td><td>59.4</td><td>13.7</td><td>18.9</td><td>8.0</td></tr>
        <tr><td>Central-south<br>America</td><td>627.2</td><td>23.9</td><td>65.2</td><td>0</td><td>10.0</td></tr>
        <tr><td>Europe</td><td>479.5</td><td>73.8</td><td>17.2</td><td>3.7</td><td>5.3</td></tr>
        <tr><td>Middle East</td><td>291.7</td><td>35.1</td><td>60.6</td><td>0</td><td>4.3</td></tr>
        <tr><td>Africa</td><td>198.5</td><td>34.3</td><td>31.9</td><td>12.3</td><td>5.3</td></tr>
        <tr><td>Asia Pacific</td><td>149.8</td><td>24.0</td><td>44.9</td><td>0</td><td>31.1</td></tr>
        <tr><td>Total</td><td>4 209.4</td><td>47.0</td><td>29.7</td><td>14.7</td><td>8.6</td></tr>
      </tbody>
    </table>
  </div>
</section>

<section class="slide s3">
  <div class="photo worker" role="img" aria-label="Engineer in hard hat and red jacket in front of a refinery tower at dusk"></div>
  <div class="brand"><span class="dot"></span>BASALT ENERGY</div>
  <h2>Get In Touch</h2>
  <p class="intro">Selerisque ligula. Maecenas eu varius risus, eu aliquet arcu. Curabitur fermentum suscipit est, tincidunt mattis lorem luctus id. Donec eget massa a diam condimentum pretium. vitae ullamcorper metus.</p>
  <div class="contact">
    <div class="row r1">
      <svg viewBox="0 0 24 24" fill="#fff"><path d="M6.6 2.5c.5-.4 1.2-.3 1.6.2l2.3 3.2c.4.5.3 1.2-.1 1.6l-1.5 1.4c.9 2 2.5 3.7 4.6 4.8l1.5-1.4c.4-.4 1.1-.5 1.6-.1l3.2 2.2c.5.4.6 1.1.2 1.6l-1.6 2.2c-.6.8-1.7 1.1-2.7.8C9.7 17.2 5.9 13.2 4.4 7.2c-.2-1 .1-2 .9-2.6z"/></svg>
      <span class="key">Phone</span><span>+123 0000 000</span>
    </div>
    <div class="row r2">
      <svg viewBox="0 0 24 24" fill="none" stroke="#fff" stroke-width="1.6"><rect x="2.5" y="5" width="19" height="14" rx="1.5"/><path d="M3 6l9 7 9-7M3 18l7-6M21 18l-7-6"/></svg>
      <span class="key">Email</span><span>mail@yourwebsite.com</span>
    </div>
    <div class="row r3">
      <svg viewBox="0 0 24 24" fill="none" stroke="#fff" stroke-width="1.4"><circle cx="12" cy="12" r="9.5"/><ellipse cx="12" cy="12" rx="4.2" ry="9.5"/><path d="M2.5 12h19M4 7h16M4 17h16"/></svg>
      <span class="key">Website</span><span>http:// yourwebsite.com</span>
    </div>
  </div>
</section>

<section class="slide s4">
  <h2>Our Icons</h2>
  <div class="icon-grid" role="img" aria-label="Set of sixty grey oil and gas industry pictograms: rigs, barrels, refineries, tankers and pipelines">
    <span class="icon"></span><span class="icon"></span><span class="icon"></span><span class="icon"></span><span class="icon"></span><span class="icon"></span><span class="icon"></span><span class="icon"></span><span class="icon"></span><span class="icon"></span><span class="icon"></span><span class="icon"></span>
    <span class="icon"></span><span class="icon"></span><span class="icon"></span><span class="icon"></span><span class="icon"></span><span class="icon"></span><span class="icon"></span><span class="icon"></span><span class="icon"></span><span class="icon"></span><span class="icon"></span><span class="icon"></span>
    <span class="icon"></span><span class="icon"></span><span class="icon"></span><span class="icon"></span><span class="icon"></span><span class="icon"></span><span class="icon"></span><span class="icon"></span><span class="icon"></span><span class="icon"></span><span class="icon"></span><span class="icon"></span>
    <span class="icon"></span><span class="icon"></span><span class="icon"></span><span class="icon"></span><span class="icon"></span><span class="icon"></span><span class="icon"></span><span class="icon"></span><span class="icon"></span><span class="icon"></span><span class="icon"></span><span class="icon"></span>
    <span class="icon"></span><span class="icon"></span><span class="icon"></span><span class="icon"></span><span class="icon"></span><span class="icon"></span><span class="icon"></span><span class="icon"></span><span class="icon"></span><span class="icon"></span><span class="icon"></span><span class="icon"></span>
  </div>
</section>

<section class="slide s5">
  <div class="photo night" role="img" aria-label="Aerial night view of an illuminated oil refinery and storage tanks, tinted navy"></div>
  <div class="closing">
    <h2>THANK YOU</h2>
    <p>FOR WATCHING THIS PRESENTATION</p>
  </div>
</section>

</body>
</html>
```